Contemporary Media Company with Logo Needs Business Card Design

Need a modern card design for a full service digital media company using the logo included. Also want the info below on the card. Probably list the services on the card back to save space for the front. Want something contemporary to impress prospective clients. You may want to submit both a somewhat more conservative design, and then a more wild one.
General Info: (this phrase need not be on the card)
Tod Parvin
Founder and CEO
949-628-4513
tod@lumavantstudio.example
lumavantstudio.example
Services: (this word need not be on the card)
Content & Experience Strategy
Brand Development
Search Engine Optimization
Website Design
Website Operation
Social Media Integration
Complete Video Solutions
Industry/Entity Type
Business
Contact Information for Business Card
Tod Parvin
Founder and CEO
949-628-4513
tod@lumavantstudio.example
lumavantstudio.example
Brand Development
Website Design
Website Operation
Social Media Integration
Complete Video Solutions
Look and feel

```html
<!DOCTYPE html>
<html lang="en">
<head>
<meta charset="utf-8">
<title>Lumavant Studio – Business Card</title>
<link rel="stylesheet" href="https://fonts.googleapis.com/css2?family=Source+Sans+3:wght@400;600&display=swap">
<style>
  :root {
    --bg-top: #1e1e1e;
    --bg-bottom: #050505;
    --card-white: #ffffff;
    --orange: #ee6a1f;
    --orange-light: #f7923a;
    --orange-deep: #e8672a;
    --orange-emboss: #e27a2e;
    --grey-text: #58595b;
    --grey-mark: #6d6e70;
    --white: #ffffff;
  }
  * { margin: 0; padding: 0; box-sizing: border-box; }
  html, body { width: 1200px; height: 900px; overflow: hidden; }
  body {
    background: linear-gradient(180deg, var(--bg-top) 0%, #141414 55%, var(--bg-bottom) 100%);
    font-family: "Source Sans 3", "Myriad Pro", sans-serif;
    position: relative;
  }
  .card {
    position: absolute;
    top: 306px;
    height: 271px;
    border-radius: 10px;
  }
  .card-front { left: 149px; width: 439px; background: var(--card-white); }
  .card-back {
    left: 608px; width: 441px;
    background: linear-gradient(180deg, var(--orange-light) 0%, var(--orange-deep) 100%);
  }
  .brand {
    position: absolute;
    display: flex;
    align-items: center;
    gap: 18px;
    font-weight: 400;
    font-size: 31px;
    letter-spacing: 2px;
    text-transform: uppercase;
    white-space: nowrap;
  }
  .brand-square { width: 52px; height: 52px; flex: none; }
  .card-front .brand { left: 45px; top: 60px; color: var(--grey-mark); }
  .card-front .brand-square { background: var(--orange); }
  .card-back .brand { left: 66px; top: 52px; color: var(--orange-emboss); }
  .card-back .brand-square { background: var(--orange-emboss); }
  .person { position: absolute; left: 138px; top: 143px; }
  .person-name { color: var(--orange); font-size: 15.5px; font-weight: 600; line-height: 18px; }
  .person-role { color: var(--grey-text); font-size: 12.5px; line-height: 16px; }
  .contacts { position: absolute; left: 138px; top: 188px; list-style: none; }
  .contacts li {
    display: flex; align-items: center; gap: 8px;
    color: var(--grey-text); font-size: 12.5px; line-height: 16px;
  }
  .contacts svg { width: 10px; height: 10px; flex: none; fill: var(--orange); }
  .services {
    position: absolute; left: 154px; top: 120px; list-style: none;
    color: var(--white); font-size: 12.5px; font-weight: 600; line-height: 18.2px;
  }
</style>
</head>
<body>
  <section class="card card-front">
    <div class="brand"><span class="brand-square"></span>Lumavant Studio</div>
    <div class="person">
      <p class="person-name">Tod Parvin</p>
      <p class="person-role">Managing Director</p>
    </div>
    <ul class="contacts">
      <li>
        <svg viewBox="0 0 10 10" aria-hidden="true"><path d="M2 0.5 L3.6 2.6 L2.6 3.6 C3.2 5 4.9 6.8 6.4 7.4 L7.4 6.4 L9.5 8 L8.3 9.5 C4.6 9.2 0.8 5.4 0.5 1.7 Z"/></svg>
        949-628-4513
      </li>
      <li>
        <svg viewBox="0 0 10 10" aria-hidden="true"><path d="M0.5 2 H9.5 V8 H0.5 Z M1.2 2.6 L5 5.4 L8.8 2.6 V2.3 H1.2 Z" fill-rule="evenodd"/></svg>
        tod@lumavantstudio.example
      </li>
      <li>
        <svg viewBox="0 0 10 10" aria-hidden="true"><circle cx="5" cy="5" r="4.5"/><path d="M0.5 5 H9.5 M5 0.5 V9.5 M5 0.5 C2.5 3 2.5 7 5 9.5 M5 0.5 C7.5 3 7.5 7 5 9.5" stroke="#fff" stroke-width="0.8" fill="none"/></svg>
        lumavantstudio.example
      </li>
    </ul>
  </section>

  <section class="card card-back">
    <div class="brand"><span class="brand-square"></span>Lumavant Studio</div>
    <ul class="services">
      <li>Content &amp; Experience Strategy</li>
      <li>Brand Development</li>
      <li>Search Engine Optimization</li>
      <li>Website Design</li>
      <li>Website Operation</li>
      <li>Social Media Integration</li>
      <li>Complete Video Solutions</li>
    </ul>
  </section>
</body>
</html>
```